Stunning Podcast Cover Design for The Morning Brook Hour!!

I need a design for my new podcast.
I will need it in a variety of size/formats, such as a large version for my podcast website homepage, the thumbnail for TuneVault, Loomcast, Pindle Store and more.

The podcast is called "The Morning Brook Hour" and it includes topics such as: business, entrepreneurship, finance, budgeting, estate planning, end-of-life planning, travel, business and personal stories featuring people from all over the world, life in general, and more.

I don't have a vision in mind so am looking for creativity but it definitely needs to have the colour gold in it somewhere! No cartoon characters please.

I will provide comments/feedback to each designer.

***UPDATE: Please see some photos of me that can be used in the podcast design.

Here is some tips on creating podcast designs. https://www.wavernest.com/blog/10-tips-create-awesome-podcast-artwork

Target Market(s)

Adults 25 - 65

Font styles to use
Other font styles liked:
• something modern - see my company logo as an example

Colors

Designer to choose colors to be used in the design.

Requirements
Must have
• The colour gold in it
Nice to have
• I feel like the word "The" should be smaller then the other three words.
• I would like to see designs with a white coloured background and a black coloured one also...
• Perhaps designs with a filter over the photo, and without.
• Perhaps use my photo, or don't use my photo!
• Please see some photos of me that can be used in the podcast design.
• Here is some tips on creating podcast designs. https://www.wavernest.com/blog/10-tips-create-awesome-podcast-artwork
Should not have
• cartoon characters
• Corny 1990's "Evenings with the Grand and Glittering" look - see https://www.clipharbor.com/watch?v=Q7T2KX8PLWZ

```html
<!DOCTYPE html>
<html lang="en">
<head>
<meta charset="utf-8">
<title>The Morning Brook Hour – Podcast Cover</title>
<link href="https://fonts.googleapis.com/css2?family=Jost:wght@600&display=swap" rel="stylesheet">
<style>
  :root {
    --paper: #ffffff;
    --pattern-tint: #e9efec;
    --frame: #3a3a3a;
    --gold: #b08d3c;
    --gold-soft: #e6d39a;
    --gold-fade: rgba(230, 211, 154, 0);
  }
  html, body {
    margin: 0;
    padding: 0;
    width: 1200px;
    height: 1200px;
    overflow: hidden;
    background: var(--paper);
  }
  .cover {
    position: relative;
    width: 1200px;
    height: 1200px;
    box-sizing: border-box;
    border: 1px solid var(--frame);
    background: var(--paper);
    overflow: hidden;
  }
  .cover__pattern {
    position: absolute;
    inset: 0;
    background: radial-gradient(circle at 60% 45%, var(--paper) 0%, var(--pattern-tint) 100%);
    opacity: 0.7;
  }
  .cover__growth {
    position: absolute;
    left: 110px;
    top: 560px;
    width: 1020px;
    height: 640px;
    background: radial-gradient(ellipse 70% 60% at 70% 70%, var(--gold-soft) 0%, var(--gold-fade) 75%);
    opacity: 0.85;
  }
  .cover__art {
    position: absolute;
    inset: 0;
  }
  .cover__title {
    font-family: "Jost", "Futura", sans-serif;
    font-weight: 600;
    fill: var(--gold);
  }
</style>
</head>
<body>
<main class="cover">
  <div class="cover__pattern" role="img" aria-label="Faint pale green pattern of dotted currency symbols"></div>
  <div class="cover__growth" role="img" aria-label="Gold rising zigzag growth arrow illustration"></div>
  <svg class="cover__art" width="1200" height="1200" viewBox="0 0 1200 1200" xmlns="http://www.w3.org/2000/svg">
    <text class="cover__title" x="68" y="198" font-size="158" textLength="276" lengthAdjust="spacingAndGlyphs">THE</text>
    <text class="cover__title" x="80" y="458" font-size="310" textLength="1062" lengthAdjust="spacingAndGlyphs">MORNING</text>
    <text class="cover__title" x="80" y="717" font-size="310" textLength="780" lengthAdjust="spacingAndGlyphs">BROOK</text>
    <text class="cover__title" x="74" y="884" font-size="168" textLength="514" lengthAdjust="spacingAndGlyphs">HOUR</text>
  </svg>
</main>
</body>
</html>
```